Company Vision Statement Design

I am trying to convert core attributes from our company's vision statement into a graphic:
1. Team
2. Partners (suppliers and customers)
3. Winning
4. Portfolio (diverse offering of beverage products beer, wine, spirits, soft drinks, and water)
5. Profitability
6. Community
I would like to only use pictures as this will accompany the longer descriptions.

Industry/Entity Type

It Company

Font styles to use
Sans Serif

Colors
0355a3

Requirements
Must have
• If there is a base color, I would prefer it is blue to match our company's logo.

```html
<!DOCTYPE html>
<html lang="en">
<head>
<meta charset="utf-8">
<title>Kelso Distributors — Our Vision</title>
<link href="https://fonts.googleapis.com/css2?family=Bebas+Neue&display=swap" rel="stylesheet">
<style>
  :root {
    --brand-blue: #0355a3;
    --ink: #ffffff;
    --watermark: rgba(255, 255, 255, 0.09);
  }
  html, body {
    margin: 0;
    padding: 0;
    width: 720px;
    height: 1200px;
    overflow: hidden;
    background: var(--brand-blue);
  }
  .vision-poster {
    position: relative;
    width: 720px;
    height: 1200px;
    overflow: hidden;
    background: var(--brand-blue);
    color: var(--ink);
    font-family: "Bebas Neue", "Arial Narrow", sans-serif;
  }
  .vision-watermark {
    position: absolute;
    left: -40px;
    top: 1200px;
    transform-origin: top left;
    transform: rotate(-90deg) scaleX(0.75);
    font-size: 440px;
    line-height: 0.8;
    white-space: nowrap;
    color: var(--watermark);
  }
  .brand-name {
    position: absolute;
    left: 18px;
    top: 30px;
    margin: 0;
    font-size: 26px;
    line-height: 1;
    letter-spacing: 1px;
    color: var(--ink);
  }
  .vision-intro {
    position: absolute;
    left: 240px;
    right: 24px;
    top: 14px;
    margin: 0;
    font-size: 22px;
    line-height: 26.5px;
    letter-spacing: 0.5px;
  }
  .line {
    display: block;
    white-space: nowrap;
    text-align: right;
  }
  .line-fill {
    white-space: normal;
    text-align: justify;
    text-align-last: justify;
  }
  .pillar-title {
    position: absolute;
    right: 24px;
    margin: 0;
    font-weight: 400;
    line-height: 0.8;
    text-align: right;
    white-space: nowrap;
  }
  .pillar-text {
    position: absolute;
    right: 24px;
    margin: 0;
    font-size: 15px;
    line-height: 19px;
    letter-spacing: 0.5px;
  }
  .pillar-team      { top: 159px;  font-size: 262px; }
  .text-team        { top: 366px;  left: 256px; }
  .pillar-partners  { top: 416px;  font-size: 120px; }
  .text-partners    { top: 512px;  left: 327px; line-height: 22px; }
  .pillar-winning   { top: 566px;  font-size: 134px; }
  .text-winning     { top: 678px;  left: 345px; }
  .pillar-portfolio { top: 733px;  font-size: 110px; }
  .text-portfolio   { top: 824px;  left: 339px; }
  .pillar-profit    { top: 874px;  font-size: 174px; }
  .text-profit      { top: 1014px; left: 326px; }
  .pillar-community { top: 1067px; font-size: 104px; }
  .text-community   { top: 1153px; left: 326px; line-height: 18px; }
</style>
</head>
<body>
<main class="vision-poster">
  <div class="vision-watermark" aria-hidden="true">OUR VISION</div>

  <p class="brand-name">KELSO</p>

  <p class="vision-intro">
    <span class="line line-fill">At Kelso, our vision is to be the best beverage</span>
    <span class="line line-fill">distributor in central and northern</span>
    <span class="line line-fill">Illinois. Our integrity and wining culture</span>
    <span class="line line-fill">enables us to exceed the expectations of our</span>
    <span class="line line-fill">customers, suppliers, and team members.</span>
  </p>

  <h2 class="pillar-title pillar-team">TEAM</h2>
  <p class="pillar-text text-team">
    <span class="line line-fill">Our team is inspired to be the best they can be. Our</span>
    <span class="line line-fill">accountable actions speak louder than our words.</span>
  </p>

  <h2 class="pillar-title pillar-partners">PARTNERS</h2>
  <p class="pillar-text text-partners">
    <span class="line">A winning network of customers and suppliers enable us</span>
    <span class="line">to create value. We want to be the distributor of choice.</span>
  </p>

  <h2 class="pillar-title pillar-winning">WINNING</h2>
  <p class="pillar-text text-winning">
    <span class="line">We are proud to win, and we are confident. Our drive</span>
    <span class="line">pushes us to beat expectations, and we settle for more.</span>
  </p>

  <h2 class="pillar-title pillar-portfolio">PORTFOLIO</h2>
  <p class="pillar-text text-portfolio">
    <span class="line line-fill">Our diverse and unique portfolio enables</span>
    <span class="line line-fill">us to meet the needs of our customers.</span>
  </p>

  <h2 class="pillar-title pillar-profit">PROFIT</h2>
  <p class="pillar-text text-profit">
    <span class="line line-fill">Maximizing profitability and long-term returns helps</span>
    <span class="line line-fill">us reinvest in our team, company, and community.</span>
  </p>

  <h2 class="pillar-title pillar-community">COMMUNITY</h2>
  <p class="pillar-text text-community">
    <span class="line line-fill">We are active in the communities we</span>
    <span class="line line-fill">serve. Giving back is part of our DNA.</span>
  </p>
</main>
</body>
</html>
```